Pine Hollow Camp Brochure Design - TRI FOLD - See text examples added

Tri- Fold Brochure designed for Remote Alaskan Wilderness Fly-in lodge.We will provide several pictures. We want activities, directions, lodge rules, history, etc... We have provided our logo. Will work on adding text.
Looking for a professional, fun, adventurous feel.
Guests must fly in to the lodge. We are completely surrounded by wilderness. 33 miles from the nearest road. Take a 30 min flight seeing trip over mountains, glaciers, rivers and wildlife with Sky Tundrix to our private airstrip. Canoe in Heron Pond. See the Moose, Caribou, Bears, Lynx, wolves, and various birds. Go gold panning in the creeks.
Accommodations include your own private cabin with private bathroom. Access to the main lodge lounge and dining rooms, wood fired sauna, covered fire pit, and use of our canoe, life jackets, and rubber boots. Meals available. Wifi in main lodge. Movies in Theater.

Target Market(s)

Adventure, photographers, hikers, mountaineers, travelers

Industry/Entity Type

Tourism

Requirements
Must have
• Logo and pictures, information - Tri-Fold
Nice to have
• High quality attractive design with logo and information
Should not have
• Cartoony feel

```html
<!DOCTYPE html>
<html lang="en">
<head>
<meta charset="utf-8">
<title>Pine Hollow Camp – Tri-Fold Brochure</title>
<link href="https://fonts.googleapis.com/css2?family=Black+Ops+One&family=Oswald:wght@300;400&family=Raleway:wght@400;600;700&display=swap" rel="stylesheet">
<style>
  :root{
    --navy:#1e2b3c;
    --red:#8c2f3d;
    --ink:#333a42;
    --paper:#ffffff;
    --stage:#d9d9de;
    --rule:#e4e4e8;
  }
  *{box-sizing:border-box;margin:0;padding:0}
  html,body{width:1200px;height:1200px;overflow:hidden}
  body{background:var(--stage);font-family:"Raleway",sans-serif;color:var(--ink);position:relative}
  .spread{position:absolute;left:200px;width:800px;height:565px;background:var(--paper);overflow:hidden;box-shadow:0 4px 14px rgba(0,0,0,.18)}
  .spread--outside{top:25px;background:linear-gradient(180deg,#fff 0%,#fff 55%,#f3f3f5 100%)}
  .spread--inside{top:610px}
  .fold{position:absolute;left:392px;top:0;width:16px;height:100%;background:linear-gradient(90deg,rgba(0,0,0,0),rgba(0,0,0,.07) 50%,rgba(0,0,0,0));z-index:5}
  .diamond{position:absolute;transform:rotate(45deg);border-radius:16px;overflow:hidden}
  .diamond--navy{background:var(--navy)}
  .diamond--red{background:var(--red)}
  .diamond--badge{background:#fff;border:1.5px solid var(--rule);display:flex;align-items:center;justify-content:center}
  .badge-name{transform:rotate(-45deg);font-weight:700;color:var(--navy);font-size:19px;line-height:1.1;text-align:center;text-transform:uppercase;letter-spacing:.5px}
  .photo--bar{background:linear-gradient(135deg,#6b3a1c,#a8643a 50%,#4a2a16)}
  .photo--lodge{background:linear-gradient(180deg,#6f9bd8 0%,#a9c6e8 45%,#8a8f3a 62%,#2d2a24 100%)}
  .photo--sheep{background:linear-gradient(160deg,#8a8c96,#e8e3b8 50%,#7c7f88)}
  .photo--cabin{background:linear-gradient(160deg,#9a9aa2,#6d6a66 45%,#2f2a26 100%)}
  .photo--porch{background:linear-gradient(150deg,#5e7a3a,#5a3d28 55%,#2e221a)}
  .photo--door{background:linear-gradient(90deg,#4a2f22,#8a5234 35%,#7a4a2e 65%,#3b2a33)}
  .photo--antlers{background:linear-gradient(150deg,#5d7a4a,#6b4a30 55%,#2f241c)}
  .photo--moose{background:linear-gradient(160deg,#8a6a48,#5a3e26 50%,#c9c0a8)}
  .cover-title{position:absolute;left:424px;top:455px}
  .cover-title__top{font-family:"Black Ops One",sans-serif;color:var(--navy);font-size:29px;letter-spacing:1px;line-height:1}
  .cover-title__bottom{font-family:"Oswald",sans-serif;font-weight:300;color:var(--red);font-size:37px;line-height:1.1;letter-spacing:.3px}
  .contact{position:absolute;left:30px;top:447px;display:flex;align-items:center;gap:22px}
  .contact__name{font-weight:700;color:var(--navy);font-size:11px;line-height:1.15;text-transform:uppercase;width:58px;text-align:center}
  .contact__list{list-style:none;font-size:11px;font-weight:700;color:var(--navy)}
  .contact__list li{display:flex;align-items:center;gap:10px;height:22px}
  .contact__list svg{width:12px;height:12px;fill:var(--red)}
  .intro{position:absolute;left:18px;top:16px;width:265px;font-size:10.4px;line-height:1.28;text-align:left;z-index:2}
  .heading{font-weight:700;color:var(--red);font-size:10px;text-transform:uppercase;letter-spacing:.3px}
  .info{position:absolute;left:18px;top:165px;width:362px}
  .info__list{list-style:none;margin-top:8px}
  .info__list li{display:flex;gap:6px;font-size:10.4px;line-height:1.3;margin-bottom:7px}
  .info__list svg{flex:none;width:10px;height:10px;margin-top:2px}
  .services{position:absolute;left:18px;top:385px;width:362px}
  .service{margin-top:6px}
  .service h3,.trip h3{font-weight:600;font-size:10.6px;color:#222;margin-bottom:3px}
  .service p,.trip p{font-size:8.4px;line-height:1.25;text-align:justify}
  .trips{position:absolute;left:418px;top:395px;width:366px}
  .trip{margin-bottom:14px}
</style>
</head>
<body>

<section class="spread spread--outside" aria-label="Brochure outside">
  <div class="diamond photo--bar" role="img" aria-label="Photo of the lodge lounge with log walls and bar" style="left:-7px;top:43px;width:196px;height:196px"></div>
  <div class="diamond diamond--navy" style="left:327px;top:-79px;width:158px;height:158px"></div>
  <div class="diamond diamond--navy" style="left:336px;top:519px;width:92px;height:92px"></div>
  <div class="diamond diamond--badge" style="left:503px;top:0px;width:170px;height:170px">
    <div class="badge-name">Pine<br>Hollow<br>Camp</div>
  </div>
  <div class="diamond photo--lodge" role="img" aria-label="Photo of the main lodge under mountains and autumn trees" style="left:365px;top:129px;width:170px;height:170px"></div>
  <div class="diamond photo--sheep" role="img" aria-label="Photo of a mounted Dall sheep" style="left:615px;top:129px;width:170px;height:170px"></div>
  <div class="diamond photo--cabin" role="img" aria-label="Photo of a log cabin with balcony" style="left:503px;top:258px;width:170px;height:170px"></div>
  <div class="diamond diamond--red" style="left:725px;top:307px;width:150px;height:150px"></div>
  <div class="fold"></div>

  <div class="contact">
    <div class="contact__name">Pine Hollow Camp</div>
    <ul class="contact__list">
      <li><svg viewBox="0 0 24 24"><path d="M6.6 10.8a15.1 15.1 0 0 0 6.6 6.6l2.2-2.2a1 1 0 0 1 1-.25 11.4 11.4 0 0 0 3.6.57 1 1 0 0 1 1 1V20a1 1 0 0 1-1 1A17 17 0 0 1 3 4a1 1 0 0 1 1-1h3.5a1 1 0 0 1 1 1c0 1.25.2 2.45.57 3.57a1 1 0 0 1-.25 1z"/></svg>+1 907-555-0148</li>
      <li><svg viewBox="0 0 24 24"><path d="M12 2a10 10 0 1 0 0 20 10 10 0 0 0 0-20zm6.9 6h-3a15.7 15.7 0 0 0-1.4-3.6A8 8 0 0 1 18.9 8zM12 4c.8 1.2 1.5 2.5 1.9 4h-3.8c.4-1.5 1.1-2.8 1.9-4zM4.3 14a8 8 0 0 1 0-4h3.4a16 16 0 0 0 0 4zm.8 2h3a15.7 15.7 0 0 0 1.4 3.6A8 8 0 0 1 5.1 16zm3-8h-3a8 8 0 0 1 4.4-3.6A15.7 15.7 0 0 0 8.1 8zM12 20c-.8-1.2-1.5-2.5-1.9-4h3.8c-.4 1.5-1.1 2.8-1.9 4zm2.3-6H9.7a14.6 14.6 0 0 1 0-4h4.6a14.6 14.6 0 0 1 0 4zm.2 5.6a15.7 15.7 0 0 0 1.4-3.6h3a8 8 0 0 1-4.4 3.6zM16.3 14a16 16 0 0 0 0-4h3.4a8 8 0 0 1 0 4z"/></svg>www.pinehollowcamp.com</li>
      <li><svg viewBox="0 0 24 24"><path d="M12 2a7 7 0 0 0-7 7c0 5.2 7 13 7 13s7-7.8 7-13a7 7 0 0 0-7-7zm0 9.5A2.5 2.5 0 1 1 12 6.5a2.5 2.5 0 0 1 0 5z"/></svg>Pine Hollow Camp, Birchfield, Alaska 99700</li>
    </ul>
  </div>

  <h1 class="cover-title">
    <span class="cover-title__top">ALASKAN</span><br>
    <span class="cover-title__bottom">WILDERNESS FLY-IN LODGE</span>
  </h1>
</section>

<section class="spread spread--inside" aria-label="Brochure inside">
  <div class="diamond photo--porch" role="img" aria-label="Photo of a cabin porch among trees" style="left:345px;top:-38px;width:190px;height:190px"></div>
  <div class="diamond photo--door" role="img" aria-label="Photo of a wooden barn-style cabin door" style="left:444px;top:93px;width:165px;height:165px"></div>
  <div class="diamond photo--antlers" role="img" aria-label="Photo of moose antlers mounted on a cabin wall" style="left:633px;top:-7px;width:150px;height:150px"></div>
  <div class="diamond photo--moose" role="img" aria-label="Photo of a mounted moose head" style="left:692px;top:159px;width:150px;height:150px"></div>
  <div class="diamond diamond--navy" style="left:344px;top:208px;width:120px;height:120px"></div>
  <div class="fold"></div>

  <p class="intro">Welcome to Pine Hollow Camp est. 1898! This is the REAL ALASKA! We are located 33 miles east of Birchfield and there are no roads to get here. Guests must fly in to the lodge. We are completely surrounded by wilderness, 33 miles from the nearest road. Take a 30 min flight seeing trip over mountains, glaciers, rivers and wildlife with Sky Tundrix to our private airstrip.</p>

  <div class="info">
    <h2 class="heading">Information</h2>
    <ul class="info__list">
      <li><svg viewBox="0 0 10 10"><circle cx="5" cy="5" r="5" fill="#1e2b3c"/><path d="M2.8 5.2l1.5 1.5 3-3" stroke="#fff" stroke-width="1.3" fill="none"/></svg>Accommodations include your own private cabin with private bathroom.</li>
      <li><svg viewBox="0 0 10 10"><circle cx="5" cy="5" r="5" fill="#1e2b3c"/><path d="M2.8 5.2l1.5 1.5 3-3" stroke="#fff" stroke-width="1.3" fill="none"/></svg>Access to the main lodge lounge and dining rooms.</li>
      <li><svg viewBox="0 0 10 10"><circle cx="5" cy="5" r="5" fill="#1e2b3c"/><path d="M2.8 5.2l1.5 1.5 3-3" stroke="#fff" stroke-width="1.3" fill="none"/></svg>Wood fired sauna.</li>
      <li><svg viewBox="0 0 10 10"><circle cx="5" cy="5" r="5" fill="#1e2b3c"/><path d="M2.8 5.2l1.5 1.5 3-3" stroke="#fff" stroke-width="1.3" fill="none"/></svg>Covered fire pit, and use of our canoe.</li>
      <li><svg viewBox="0 0 10 10"><circle cx="5" cy="5" r="5" fill="#1e2b3c"/><path d="M2.8 5.2l1.5 1.5 3-3" stroke="#fff" stroke-width="1.3" fill="none"/></svg>life jackets, and rubber boots.</li>
      <li><svg viewBox="0 0 10 10"><circle cx="5" cy="5" r="5" fill="#1e2b3c"/><path d="M2.8 5.2l1.5 1.5 3-3" stroke="#fff" stroke-width="1.3" fill="none"/></svg>Meals available.</li>
      <li><svg viewBox="0 0 10 10"><circle cx="5" cy="5" r="5" fill="#1e2b3c"/><path d="M2.8 5.2l1.5 1.5 3-3" stroke="#fff" stroke-width="1.3" fill="none"/></svg>Wifi in main lodge.</li>
      <li><svg viewBox="0 0 10 10"><circle cx="5" cy="5" r="5" fill="#1e2b3c"/><path d="M2.8 5.2l1.5 1.5 3-3" stroke="#fff" stroke-width="1.3" fill="none"/></svg>Movies in Theater.</li>
    </ul>
  </div>

  <div class="services">
    <h2 class="heading">Services</h2>
    <div class="service">
      <h3>Hiking 10 local trails</h3>
      <p>All trails begin at the lodge. Take Larkspur trail to the boreal forest for bird and wildlife watching. Hike to Heron Pond or Alder Pond. Climb the trail up Mt. Carrow and view the Dall Sheep. Take Grey Knob trail for a hike above the trees. Many More! - Rubber Boots, Bear Spray, maps</p>
    </div>
    <div class="service">
      <h3>Nightly Bed and Breakfast in our Cabins</h3>
      <p>Stay in one of our private cabins with private bathroom, hot water, baseboard heat or wood stove for $139/night. Most rooms have 1 Queen and 1 twin bed. Breakfast included. Optional Lunch and Dinner at $20/person.</p>
    </div>
  </div>

  <div class="trips">
    <div class="trip">
      <h3>Flight Seeing trips</h3>
      <p>Take a Kestrel 6 or Turbo Loon from Birchfield, across glaciers, mountains, rivers, lakes and myriad wildlife. Land at Pine Hollow Camp and stay as many days as you like. Then take another route back to the airport on your outbound trip! $300 each way. Or book the plane for $600 each way</p>
    </div>
    <div class="trip">
      <h3>Canoeing on Heron Pond!</h3>
      <p>Paddle our canoe around Heron Pond. Photograph the swans, ducks, or other wildlife. Canoe, Paddles, Life Jackets, Rubber boots provided.</p>
    </div>
  </div>
</section>

</body>
</html>
```